Iron and home washing service

I provide I home iron and washing service for adult and kids clothes on a smoke pet free environment. I can collect and offer a next day delivery. Or same day depend on items and volume. I offer competitive frendly and reliable service and price. I charge by weight £4,50 / kg. approx 5 items =1 kg minimum for collection.

```html
<!DOCTYPE html>
<html lang="en">
<head>
<meta charset="utf-8">
<title>Iron and Home Washing Service</title>
<link href="https://fonts.googleapis.com/css2?family=Michroma&family=Roboto:wght@400;500;700&family=Roboto+Condensed:wght@700&display=swap" rel="stylesheet">
<style>
  :root {
    --charcoal: #262626;
    --charcoal-light: #4a4a4a;
    --orange: #e8531f;
    --orange-light: #f37a26;
    --ribbon-red: #b3231c;
    --yellow: #ffe600;
    --cream: #fff3c4;
    --white: #ffffff;
    --ink: #111111;
    --site-grey: #3a3a3a;
    --photo-light: #f1ece6;
    --photo-warm: #d9a58a;
  }
  html, body { margin: 0; padding: 0; overflow: hidden; background: #ffffff; }
  .flyer {
    position: relative;
    width: 1200px;
    height: 873px;
    overflow: hidden;
    font-family: "Roboto", Arial, sans-serif;
  }
  .flyer-art { position: absolute; inset: 0; }
  .text { position: absolute; margin: 0; white-space: nowrap; }

  .kicker {
    top: 60px; left: 335px; transform: translateX(-50%);
    font-family: "Michroma", sans-serif;
    font-size: 32px; letter-spacing: 6px; color: var(--white);
    display: flex; align-items: center; gap: 18px;
  }
  .kicker::before, .kicker::after {
    content: ""; width: 62px; height: 2px; background: var(--white);
  }
  .headline {
    top: 118px; left: 335px; transform: translateX(-50%);
    font-family: "Roboto Condensed", sans-serif; font-weight: 700;
    font-size: 50px; color: var(--yellow);
  }
  .band-line { left: 42px; font-size: 31px; font-weight: 500; }
  .band-line.dark { top: 226px; color: var(--ink); }
  .band-line.bright { top: 271px; color: var(--yellow); font-size: 38px; }

  .offer-title {
    top: 458px; left: 325px; transform: translateX(-50%);
    font-family: "Michroma", sans-serif; font-size: 22px; letter-spacing: 3px;
    color: var(--cream); text-decoration: underline; text-underline-offset: 6px;
  }
  .offer-body {
    top: 508px; left: 325px; transform: translateX(-50%);
    text-align: center; font-size: 20px; font-weight: 500; line-height: 30px;
    color: var(--ink);
  }
  .pricing {
    top: 648px; left: 42px;
    font-family: "Michroma", sans-serif; font-size: 22px; letter-spacing: 4px;
    line-height: 41px; color: var(--white);
  }
  .call {
    top: 807px; left: 42px; font-size: 30px; font-weight: 500; color: var(--yellow);
  }
  .call .phone { color: var(--white); font-size: 34px; margin-left: 6px; }
  .website {
    top: 62px; left: 760px; font-size: 30px; font-weight: 500; color: var(--site-grey);
  }
</style>
</head>
<body>
<main class="flyer">
  <svg class="flyer-art" width="1200" height="873" viewBox="0 0 1200 873">
    <defs>
      <radialGradient id="silk-sheen" cx="0.35" cy="0.4" r="0.7">
        <stop offset="0" stop-color="var(--charcoal-light)"/>
        <stop offset="0.6" stop-color="#333333"/>
        <stop offset="1" stop-color="var(--charcoal)"/>
      </radialGradient>
      <linearGradient id="orange-band" x1="0" y1="0" x2="1" y2="0">
        <stop offset="0" stop-color="var(--orange)"/>
        <stop offset="1" stop-color="var(--orange-light)"/>
      </linearGradient>
      <linearGradient id="photo-tone" x1="0" y1="0" x2="1" y2="1">
        <stop offset="0" stop-color="var(--photo-light)"/>
        <stop offset="0.6" stop-color="#e8d6cb"/>
        <stop offset="1" stop-color="var(--photo-warm)"/>
      </linearGradient>
    </defs>

    <rect class="dark-panel" width="1200" height="873" fill="url(#silk-sheen)"/>
    <rect class="audience-band" x="0" y="208" width="900" height="124" fill="url(#orange-band)"/>
    <polygon class="ribbon-fold" points="0,332 900,332 900,427 650,427 0,362" fill="var(--ribbon-red)"/>
    <rect class="offer-box" x="0" y="427" width="650" height="168" fill="url(#orange-band)"/>
    <rect class="call-band" x="0" y="792" width="900" height="81" fill="url(#orange-band)"/>

    <path class="curve-accent" d="M 590 0 Q 870 436 660 873 L 710 873 Q 910 436 650 0 Z" fill="var(--orange)"/>
    <path class="photo-area" role="img" aria-label="Photo of a smiling mother helping her young daughter iron clothes"
          d="M 650 0 Q 910 436 700 873 L 1200 873 L 1200 0 Z" fill="url(#photo-tone)"/>
    <path class="curve-line" d="M 650 0 Q 910 436 700 873" fill="none" stroke="var(--yellow)" stroke-width="10"/>
  </svg>

  <p class="text kicker">IRON AND</p>
  <h1 class="text headline">HOME WASHING SERVICE</h1>
  <p class="text band-line dark">FOR ADULT AND KIDS CLOTHES ON A</p>
  <p class="text band-line bright">SMOKE PET FREE ENVIRONMENT</p>
  <p class="text offer-title">I CAN COLLECT AND OFFER</p>
  <p class="text offer-body">A NEXT DAY DELIVERY OR SAME DAY DEPEND ON<br>ITEMS AND VOLUME</p>
  <p class="text pricing">I CHARGE BY WEIGHT £4,50 / KG.<br>APPROX 5 ITEMS =1 KG MINIMUM<br>FOR COLLECTION.</p>
  <p class="text call">CALL US TODAY: <span class="phone">XXX-XXX-XXXX</span></p>
  <p class="text website">www.yourwebsite.com</p>
</main>
</body>
</html>
```